Ledgerwise Capital Business Cards

We are looking to revamp the current business cards each of our locations uses. We are a lending company that specializes in personal loans, title loans, and tax services. We have locations in New Mexico, Texas, and Oklahoma.

We would like a cleaner, sleeker look while still highlighting what we offer. Title Loans, Personal Loans & Tax Services. We also want to include our referral fee somewhere on the card. We would like to see an English option as well as a Spanish option for the cards.

PLEASE NOTE: Some business cards do not include the employee's name but just the store's location, while others will include both.

These are double-sided business cards, and we would like to see proof if possible. I have included proofs of our current business cards for you to review below, as well as our company logo. Feel free to get creative with the logo, etc! Colors should match the logo; however, you do not need to use all of our logo colors if you don't want to.

```html
<!DOCTYPE html>
<html lang="en">
<head>
<meta charset="utf-8">
<title>Ledgerwise Capital Business Cards</title>
<link href="https://fonts.googleapis.com/css2?family=Montserrat:wght@400;500;600;800&display=swap" rel="stylesheet">
<style>
  :root {
    --green: #165232;
    --green-deep: #124a2c;
    --red: #c41e27;
    --white: #ffffff;
    --backdrop: #2b2b2b;
  }
  * { box-sizing: border-box; margin: 0; padding: 0; }
  html, body { width: 1200px; height: 1000px; overflow: hidden; }
  body {
    background: var(--backdrop);
    font-family: "Montserrat", sans-serif;
    position: relative;
  }
  .card {
    position: absolute;
    left: 190px;
    width: 820px;
    height: 469px;
    border-radius: 26px;
    overflow: hidden;
    box-shadow: 0 10px 30px rgba(0,0,0,.45);
  }
  .card svg.card-art { position: absolute; inset: 0; width: 100%; height: 100%; }

  /* Front */
  .card-front { top: 20px; background: var(--green); }
  .brand {
    position: absolute;
    left: 0; right: 0;
    text-align: center;
  }
  .brand-name {
    display: inline-flex;
    align-items: center;
    gap: 12px;
    font-weight: 600;
    font-size: 42px;
    letter-spacing: .5px;
  }
  .brand-dot { width: 14px; height: 14px; border-radius: 50%; background: var(--red); }
  .brand-url {
    display: block;
    color: var(--red);
    font-weight: 500;
    font-size: 18px;
    letter-spacing: 1px;
    margin-top: 4px;
  }
  .card-front .brand { top: 95px; }
  .card-front .brand-name { color: var(--white); }
  .referral-pill {
    position: absolute;
    left: 50%;
    top: 222px;
    transform: translateX(-50%);
    padding: 6px 34px;
    border: 2px solid var(--red);
    border-radius: 30px;
    background: var(--green);
    color: var(--white);
    font-weight: 800;
    font-size: 34px;
    letter-spacing: 2px;
    white-space: nowrap;
  }
  .referral-offer {
    position: absolute;
    left: 0; right: 0;
    top: 300px;
    text-align: center;
    color: var(--white);
    font-weight: 800;
    font-size: 44px;
    letter-spacing: 3px;
  }
  .referral-offer .amount { color: var(--red); }

  /* Back */
  .card-back { top: 511px; background: var(--white); }
  .staff {
    position: absolute;
    left: 40px;
    top: 124px;
    color: var(--white);
  }
  .staff-name { font-weight: 800; font-size: 30px; letter-spacing: 2px; line-height: 1.1; }
  .staff-role { font-size: 18px; letter-spacing: 1px; }
  .contact {
    position: absolute;
    left: 40px;
    top: 264px;
    color: var(--white);
    font-size: 18px;
    line-height: 1.55;
    letter-spacing: .8px;
    list-style: none;
  }
  .contact li { display: flex; align-items: center; gap: 10px; }
  .contact svg { width: 16px; height: 16px; flex: none; }
  .card-back .brand { left: auto; right: 50px; top: 120px; text-align: right; }
  .card-back .brand-name { color: var(--green); font-size: 38px; }
  .services {
    position: absolute;
    right: 50px;
    bottom: 34px;
    list-style: none;
    text-align: right;
    color: var(--white);
    font-size: 21px;
    line-height: 1.5;
    letter-spacing: 1.5px;
  }
  .services li::after { content: " •"; color: var(--red); }
</style>
</head>
<body>

  <section class="card card-front" aria-label="Card front">
    <svg class="card-art" viewBox="0 0 820 469" aria-hidden="true">
      <line x1="0" y1="245" x2="820" y2="245" stroke="var(--red)" stroke-width="1.5"/>
    </svg>
    <div class="brand">
      <span class="brand-name"><span class="brand-dot"></span>Ledgerwise Capital</span>
      <span class="brand-url">www.ledgerwisecapital.com</span>
    </div>
    <div class="referral-pill">Refer a Friend</div>
    <p class="referral-offer">GET UP TO <span class="amount">$100</span></p>
  </section>

  <section class="card card-back" aria-label="Card back">
    <svg class="card-art" viewBox="0 0 820 469" aria-hidden="true">
      <polygon points="0,208 820,308 820,469 0,469" fill="var(--green)"/>
      <path d="M0,115 L318,115 Q345,115 356,140 L390,247.6 L0,200 Z" fill="var(--red)"/>
      <polygon points="390,240.6 820,293 820,300 390,247.6" fill="var(--red)"/>
    </svg>

    <div class="staff">
      <p class="staff-name">JANE DOE</p>
      <p class="staff-role">Branch manager</p>
    </div>

    <ul class="contact">
      <li>123 Elm Street, Suite B</li>
      <li>Anytown, Texas 55555</li>
      <li>
        <svg viewBox="0 0 16 16" aria-hidden="true"><path fill="var(--red)" d="M3 2h3l1 3-2 1a8 8 0 0 0 5 5l1-2 3 1v3a1 1 0 0 1-1 1A12 12 0 0 1 2 3a1 1 0 0 1 1-1z"/></svg>
        (505) 555-1212
      </li>
      <li>
        <svg viewBox="0 0 16 16" aria-hidden="true"><rect x="1" y="4" width="14" height="9" rx="1" fill="var(--red)"/><path d="M1.5 4.5 8 9l6.5-4.5" stroke="var(--white)" stroke-width="1.2" fill="none"/></svg>
        abcde@ledgerwisecapital.com
      </li>
    </ul>

    <div class="brand">
      <span class="brand-name"><span class="brand-dot"></span>Ledgerwise Capital</span>
      <span class="brand-url">www.ledgerwisecapital.com</span>
    </div>

    <ul class="services">
      <li>Title Loans</li>
      <li>Personal Loans</li>
      <li>Tax Services</li>
    </ul>
  </section>

</body>
</html>
```